Will you marry me post card

I am just looking for a postcard to send my partner that will ask him to marry me.
I plan on creating about 200 of them and mailing them all at once so that he gets them all on the same day.
They should all be similar or could have a few different options.
I would like it simple, elegant, clean and crisp. No images, just text or icons

My only requirement is the text, "will you marry me?" in all lowercase -- any fonts, can be big, small, varying sizes, repeated, whole card, tiny space, don't care...just amazing design. BUT SIMPLE!

```html
<!DOCTYPE html>
<html lang="en">
<head>
<meta charset="utf-8">
<title>will you marry me? — postcard</title>
<link href="https://fonts.googleapis.com/css2?family=Inconsolata:wght@400;500&display=swap" rel="stylesheet">
<style>
  :root {
    --backdrop: #5e4129;
    --card: #ffffff;
    --ink: #111111;
    --accent: #e3262b;
    --stamp-line: #9a9a9a;
    --rule: #1a1a1a;
    --icon-fill: #2a2a2a;
  }
  * { box-sizing: border-box; margin: 0; padding: 0; }
  html, body {
    width: 942px;
    height: 1200px;
    overflow: hidden;
    background: var(--backdrop);
  }
  .canvas {
    position: relative;
    width: 942px;
    height: 1200px;
  }
  .postcard {
    position: absolute;
    left: 111px;
    width: 720px;
    height: 557px;
    background: var(--card);
    box-shadow: 0 6px 18px rgba(0, 0, 0, 0.35);
  }
  .postcard--front { top: 30px; }
  .postcard--back { top: 613px; }

  .proposal {
    position: absolute;
    left: 302px;
    top: 374px;
    font-family: "Inconsolata", monospace;
    font-weight: 500;
    font-size: 24px;
    line-height: 1;
    letter-spacing: 6px;
    color: var(--ink);
    white-space: nowrap;
  }
  .proposal__accent { color: var(--accent); }

  .ring-motif {
    position: absolute;
    left: 97px;
    top: 66px;
    width: 86px;
    height: 95px;
    border-radius: 50%;
    background: radial-gradient(circle, var(--icon-fill) 0%, #6a6a6a 100%);
  }
  .stamp-box {
    position: absolute;
    left: 593px;
    top: 64px;
    width: 89px;
    height: 108px;
    border: 1.5px solid var(--stamp-line);
  }
  .address-lines {
    position: absolute;
    left: 383px;
    top: 249px;
    width: 299px;
  }
  .address-lines__rule {
    height: 0;
    border-top: 2px solid var(--rule);
    margin-bottom: 59px;
  }
</style>
</head>
<body>
<main class="canvas">
  <section class="postcard postcard--front" aria-label="Postcard front">
    <p class="proposal">will you <span class="proposal__accent">marry</span> me?</p>
  </section>

  <section class="postcard postcard--back" aria-label="Postcard back">
    <div class="ring-motif" role="img" aria-label="Wedding rings icon with a diamond"></div>
    <div class="stamp-box" aria-label="Stamp area"></div>
    <div class="address-lines" aria-label="Address lines">
      <div class="address-lines__rule"></div>
      <div class="address-lines__rule"></div>
      <div class="address-lines__rule"></div>
    </div>
  </section>
</main>
</body>
</html>
```